Need to make a work slip for trucking company.

I need a form to fill out for my truck drivers to get signed on delivery. It is for a trucking company and this form will be for each machine equipment move. I have included my old sheet which I need Updated. Its going on a 9.5 inch by 8.5 inch sheet of paper. It should have room for the day, date, customer name, ordered by, P.O. Number, Project Number, Driver, Truck/Trailer, Tolls (needs more room then my old sheet need a few lines under each other for each toll during the machine move), Permits, some room for other information, Loads, Hours, and 2 lines for a Signature and Print Line.
Updates

Need to also include a Pickup Address and a Deliver Address with lines to write in. Also I need to add a Print Line (and labeled Print) for whoever is signing the ticket.

Requirements
Must have
• My new company name and Logo. I have included my new Logo. It must be easy to ready. Must include my company colors. (Concrete Gray, and Neon Blue)

```html
<!DOCTYPE html>
<html lang="en">
<head>
<meta charset="utf-8">
<title>Work Slip – Q-Line Haulage</title>
<link href="https://fonts.googleapis.com/css2?family=Mulish:wght@400;600;800&display=swap" rel="stylesheet">
<style>
  :root {
    --page-bg: #eaeef2;
    --sheet: #ffffff;
    --sheet-tint: #fafafa;
    --brand-blue: #1a6fc0;
    --neon-blue: #3aa9dc;
    --concrete: #7d7d80;
    --concrete-faint: #cfc7c5;
    --ink: #1e1e1e;
    --rule: #c4c4c4;
    --chip: #e7e7e7;
  }
  * { box-sizing: border-box; margin: 0; padding: 0; }
  html, body { width: 800px; height: 1200px; overflow: hidden; }
  body {
    background: var(--page-bg);
    font-family: "Mulish", Arial, sans-serif;
    color: var(--ink);
    position: relative;
  }
  .work-slip {
    position: absolute;
    left: 20px; top: 150px;
    width: 760px; height: 900px;
    background: var(--sheet);
    overflow: hidden;
    box-shadow: 0 2px 10px rgba(0,0,0,.08);
  }
  .body-tint {
    position: absolute; left: 0; right: 0; top: 211px; bottom: 0;
    background: var(--sheet-tint);
  }
  .decor-top {
    position: absolute; left: 0; top: 0; width: 390px; height: 160px;
    background: linear-gradient(135deg, rgba(58,169,220,.16), rgba(58,169,220,0) 70%);
  }
  .decor-bottom {
    position: absolute; right: 0; bottom: 0; width: 300px; height: 150px;
    background: linear-gradient(315deg, rgba(160,160,165,.14), rgba(160,160,165,0) 70%);
  }
  .brand {
    position: absolute; right: 34px; top: 26px;
    text-align: right;
  }
  .brand-name {
    font-weight: 800; font-size: 34px; letter-spacing: -0.5px;
    color: var(--brand-blue); line-height: 1; white-space: nowrap;
  }
  .brand-contact {
    margin-top: 22px;
    color: var(--brand-blue); font-size: 15px; line-height: 20px;
  }
  .brand-contact .sep { padding: 0 8px; }
  .brand-bar {
    position: absolute; right: 0; top: 24px; width: 15px; height: 104px;
    background: var(--brand-blue);
  }
  .chip {
    display: inline-block; background: var(--chip);
    border-radius: 2px; padding: 2px 5px; font-size: 15px; line-height: 20px;
  }
  .day-row { position: absolute; left: 33px; top: 157px; display: flex; gap: 4px; }
  .day-row .chip { width: 23px; text-align: center; padding: 2px 0; }
  .meridiem { position: absolute; left: 249px; top: 157px; display: flex; gap: 4px; }
  .date-field {
    position: absolute; left: 426px; top: 157px; display: flex; gap: 5px; align-items: center;
    font-size: 15px;
  }
  .date-box { width: 256px; height: 24px; background: var(--chip); border-radius: 2px; }
  .field {
    position: absolute; display: flex; align-items: flex-end; gap: 5px;
    font-size: 14.5px; line-height: 18px; white-space: nowrap;
  }
  .field .rule { flex: 1; border-bottom: 1px solid var(--rule); height: 14px; }
  .rule-only { position: absolute; border-bottom: 1px solid var(--rule); height: 1px; }
  .full { left: 36px; width: 692px; }
  .short { left: 36px; width: 400px; }
  .equipment {
    position: absolute; left: 100px; top: 326px; display: flex; gap: 5px;
  }
  .equipment .chip { padding: 2px 6px; }
  .watermark {
    position: absolute; right: 40px; bottom: 40px;
    font-weight: 800; font-size: 30px; color: var(--concrete-faint);
    letter-spacing: -0.5px; white-space: nowrap;
  }
</style>
</head>
<body>
  <main class="work-slip">
    <div class="body-tint"></div>
    <div class="decor-top" role="img" aria-label="Light blue geometric line pattern"></div>
    <div class="decor-bottom" role="img" aria-label="Faint grey geometric line pattern"></div>

    <header class="brand">
      <div class="brand-name">Q-LINE HAULAGE</div>
      <div class="brand-contact">
        <div>Harbor Point, New York 10000</div>
        <div>Phone (555) 410 -2200<span class="sep">|</span>Fax&nbsp; (555) 410 -2209</div>
      </div>
    </header>
    <div class="brand-bar"></div>

    <div class="day-row">
      <span class="chip">M</span><span class="chip">T</span><span class="chip">W</span><span class="chip">T</span><span class="chip">F</span><span class="chip">S</span><span class="chip">S</span>
    </div>
    <div class="meridiem"><span class="chip">A.M.</span><span class="chip">P.M.</span></div>
    <div class="date-field"><span>Date:</span><span class="date-box"></span></div>

    <div class="field full" style="top:221px"><span>Customer:</span><span class="rule"></span></div>
    <div class="field full" style="top:256px"><span>Ordered By:</span><span class="rule"></span></div>
    <div class="field" style="top:291px; left:36px; width:320px"><span>P.O. No.:</span><span class="rule"></span></div>
    <div class="field" style="top:291px; left:379px; width:349px"><span>Project No.:</span><span class="rule"></span></div>

    <div class="equipment">
      <span class="chip">F/B</span><span class="chip">L/B</span><span class="chip">LD</span><span class="chip">STR/TRL</span><span class="chip">BM/TK</span><span class="chip">DUMP TK</span><span class="chip">ROLL BACK</span><span class="chip">ROLL OFF</span>
    </div>

    <div class="field full" style="top:372px"><span>Pickup Address</span><span class="rule"></span></div>
    <div class="field full" style="top:407px"><span>Delivery Address</span><span class="rule"></span></div>
    <div class="field full" style="top:442px"><span>Driver</span><span class="rule"></span></div>
    <div class="field full" style="top:477px"><span>Tr. / Eq.</span><span class="rule"></span></div>
    <div class="field full" style="top:512px"><span>L / W / H</span><span class="rule"></span></div>
    <div class="field full" style="top:547px"><span>Tolls</span><span class="rule"></span></div>
    <div class="rule-only full" style="top:580px"></div>
    <div class="rule-only full" style="top:610px"></div>
    <div class="field full" style="top:636px"><span>Permit(s)</span><span class="rule"></span></div>
    <div class="rule-only full" style="top:668px"></div>
    <div class="field full" style="top:694px"><span>Other</span><span class="rule"></span></div>
    <div class="rule-only full" style="top:726px"></div>

    <div class="field short" style="top:756px"><span>Loads</span><span class="rule"></span></div>
    <div class="field short" style="top:788px"><span>Hours</span><span class="rule"></span></div>
    <div class="field short" style="top:822px"><span>Signature</span><span class="rule"></span></div>
    <div class="field short" style="top:856px"><span>Print</span><span class="rule"></span></div>

    <div class="watermark">Q-LINE HAULAGE</div>
  </main>
</body>
</html>
```